Flaschenetikett für Nahrungsergänzungsmittel
Zielgruppe
Wir betreiben eine Naturheilpraxis für Mensch und Tier.
Neben der Behandlung von Menschen und Tieren soll der Verkauf von Nahrungsergänzungsmitteln ausgebaut werden.
Unsere Zielgruppe sind Verbraucher, die der Naturheilkunde und traditionellen Naturheilmitteln zugewandt sind.
Aufgabenstellung
Entstehen soll ein Flaschenetikett für 'Kolloidales Silber'. Es gibt eine Vorder- und eine Rückseite.
Zukünftig werden verschiedene Produkte bzw. Nahrungsergänzungsmittel zum Verkauf angeboten. Damit ein gewisser Wiedererkennungswert entsteht, sollen die einzelnen Etiketten von der Art gleich/ähnlich sein und sich nur durch bestimmte Formen oder Farben unterscheiden.
Unser bestehendes Logo finden sie anbei.
Hier der Link zur verwendeten 1000ml Braunglasflasche.
https://www.gebindor.de/flaschen/glasflaschen/meplatflasche/7312/1000-ml-meplatflasche-glas-braun-pp-28-meplat
Wünschenswert wäre, wenn das Etikett auf eine 500ml Flasche skaliert werden könnte.
Hier der Link zur verwendeten 500ml Braunglasflasche.
https://www.gebindor.de/flaschen/glasflaschen/meplatflasche/7311/500-ml-meplatflasche-glas-braun-pp-28-meplat
Das Produkt wird sowohl beim Tier als auch beim Menschen angewendet.
Die Form des Etiketts muss nicht zwingend der Flaschenform entsprechen.
Beispiele, die uns gut gefallen:
https://www.tulpenkrug.de/collections/limonaden-essencen
https://www.moosquell.bio/vitarel-feldblume-10-kraeuter-ferment-510ml?c=48

```html
<!DOCTYPE html>
<html lang="de">
<head>
<meta charset="utf-8">
<title>Kolloidales Silber – Flaschenetiketten</title>
<link rel="stylesheet" href="https://fonts.googleapis.com/css2?family=Barlow:wght@500&family=Oswald:wght@500;600&family=Handlee&family=Courier+Prime&display=swap">
<style>
  :root{
    --teal:#67c1bb;
    --ink:#3e3d42;
    --paper:#ffffff;
    --backdrop:#e9e9e9;
    --silver:#b4b5b8;
    --sage:#6b7d56;
    --sand:#c29a6c;
    --stone:#bdbec0;
  }
  *{box-sizing:border-box;margin:0;padding:0}
  html,body{width:1200px;height:901px;overflow:hidden}
  body{background:var(--backdrop);position:relative;font-family:"Oswald",sans-serif;color:var(--ink)}

  .size-caption{position:absolute;font:600 9.5px/1 "Oswald",sans-serif;letter-spacing:.04em;color:#222;text-align:center}
  .size-caption--500{left:294px;width:212px;top:203px}
  .size-caption--1000{left:589px;width:309px;top:45px}

  .label{position:absolute;width:calc(309px*var(--s));display:flex;flex-direction:column;background:var(--paper)}
  .label--500{--s:.686;left:294px;top:220px;height:494px}
  .label--1000{--s:1;left:589px;top:65px;height:649px}

  .label__header{height:calc(79px*var(--s));background:var(--teal);color:var(--paper);text-align:center;font-family:"Barlow",sans-serif;font-weight:500;padding-top:calc(17px*var(--s))}
  .brand-name{font-size:calc(14px*var(--s));letter-spacing:.1em;line-height:1.1}
  .brand-tagline{font-size:calc(9.5px*var(--s));letter-spacing:.05em;line-height:1.2}
  .brand-owners{font-size:calc(7px*var(--s));letter-spacing:.03em;line-height:1.4;opacity:.95}
  .label__rule{height:calc(5px*var(--s));background:var(--ink)}

  .label__emblem{height:calc(183px*var(--s));display:flex;align-items:center;justify-content:center;padding-bottom:calc(16px*var(--s))}
  .emblem-art{width:calc(150px*var(--s));height:calc(108px*var(--s));border-radius:50%;background:radial-gradient(circle at 50% 45%,#f4f4f5 0,#d9dadc 55%,#a9aaad 100%)}

  .label__body{flex:1;position:relative;background:var(--teal);border-top:calc(4px*var(--s)) solid var(--ink);padding:calc(53px*var(--s)) calc(34px*var(--s)) 0 calc(32px*var(--s))}
  .product-title{position:absolute;left:50%;top:calc(-16px*var(--s));transform:translateX(-50%);width:calc(254px*var(--s));height:calc(37px*var(--s));background:var(--paper);border-radius:0 0 calc(10px*var(--s)) calc(10px*var(--s));text-align:center;font:400 calc(29px*var(--s))/calc(36px*var(--s)) "Handlee",cursive;white-space:nowrap}
  .product-title__first{color:var(--teal)}
  .product-title__second{color:var(--silver)}

  .product-claim{font:600 calc(21px*var(--s))/1 "Oswald",sans-serif;text-transform:uppercase;letter-spacing:-.01em;padding-bottom:calc(8px*var(--s))}
  .divider{border:0;border-top:calc(1.2px*var(--s)) solid var(--paper);margin:0 0 calc(14px*var(--s))}
  .facts{font:500 calc(8px*var(--s))/calc(12px*var(--s)) "Oswald",sans-serif;text-transform:uppercase;letter-spacing:.03em;margin-bottom:calc(11px*var(--s))}
  .facts--storage{margin-bottom:calc(10px*var(--s))}
  .facts__spacer{height:calc(10px*var(--s))}

  .dosage{display:flex;align-items:flex-end;gap:calc(10px*var(--s))}
  .dosage__options{font:500 calc(8.5px*var(--s))/1.2 "Oswald",sans-serif;text-transform:uppercase}
  .dosage__choices{display:flex;gap:calc(5px*var(--s));margin-top:calc(3px*var(--s))}
  .choice{display:flex;align-items:center}
  .choice__box{display:inline-block;width:calc(12px*var(--s));height:calc(12px*var(--s));background:var(--paper);border:calc(1px*var(--s)) solid var(--ink);margin-right:1px}
  .dosage__volume{border-left:calc(1.2px*var(--s)) solid var(--paper);padding-left:calc(10px*var(--s));font:600 calc(20px*var(--s))/1 "Oswald",sans-serif;height:calc(30px*var(--s));display:flex;align-items:flex-end}

  .label__footer{height:calc(88px*var(--s));margin-top:calc(5px*var(--s));background:var(--ink);color:var(--paper);display:flex;justify-content:space-between;padding:calc(24px*var(--s)) calc(34px*var(--s)) 0 calc(32px*var(--s))}
  .maker{font:500 calc(6px*var(--s))/calc(11px*var(--s)) "Oswald",sans-serif;text-transform:uppercase;letter-spacing:.06em}
  .lot__label{font:500 calc(5.5px*var(--s))/1 "Oswald",sans-serif;text-transform:uppercase;margin:calc(4px*var(--s)) 0 calc(4px*var(--s))}
  .lot__box{width:calc(67px*var(--s));height:calc(28px*var(--s));background:var(--paper);color:var(--ink);font:400 calc(7.5px*var(--s))/calc(9.5px*var(--s)) "Courier Prime",monospace;padding:calc(4px*var(--s)) calc(10px*var(--s));letter-spacing:.05em}

  .palette{position:absolute;left:401px;right:0;bottom:0;height:22px;display:flex}
  .palette__swatch{flex:1}
  .palette__swatch--teal{background:var(--teal)}
  .palette__swatch--sage{background:var(--sage)}
  .palette__swatch--sand{background:var(--sand)}
  .palette__swatch--stone{background:var(--stone)}
  .palette__swatch--ink{background:var(--ink)}
</style>
</head>
<body>

<div class="size-caption size-caption--500">128X55MM</div>
<article class="label label--500">
  <header class="label__header">
    <div class="brand-name">KRAEUTERWINKL</div>
    <div class="brand-tagline">FÜR MENSCH &amp; TIER</div>
    <div class="brand-owners">Lena Brandt &amp; Tobias Merz</div>
  </header>
  <div class="label__rule"></div>
  <div class="label__emblem">
    <div class="emblem-art" role="img" aria-label="Illustration: Frau und Hund sitzend in einem Kreis mit Blättern"></div>
  </div>
  <section class="label__body">
    <div class="product-title"><span class="product-title__first">Kolloidales</span> <span class="product-title__second">Silber</span></div>
    <h1 class="product-claim">Antimikrobielle Lösung</h1>
    <hr class="divider">
    <p class="facts">Destilliertes Wasser entmineralisiert<br>Feinsilber Reinheit &gt; 99,99%<br>Kein Lebensmittel</p>
    <hr class="divider">
    <p class="facts facts--storage">Lagerung:<br>Bei Zimmertemperatur dunkel und außerhalb der Reichweite von Kindern lagern. Jegliche Nähe zu elektromagnetischen Feldern vermeiden und nicht mit Metall in Verbindung bringen.</p>
    <p class="facts">Nach dem Öffnen innerhalb von 12 Wochen aufbrauchen</p>
    <hr class="divider">
    <div class="dosage">
      <div class="dosage__options">Konzentration:
        <div class="dosage__choices">
          <span class="choice"><span class="choice__box"></span>25PPM</span>
          <span class="choice"><span class="choice__box"></span>50PPM</span>
          <span class="choice"><span class="choice__box"></span>75PPM</span>
          <span class="choice"><span class="choice__box"></span>100PPM</span>
        </div>
      </div>
      <div class="dosage__volume">500ML</div>
    </div>
  </section>
  <footer class="label__footer">
    <div class="maker">Hergestellt in Deutschland von:<br>Tobias Merz, Lena Brandt GbR<br>info.kraeuterwinkl@postfach.de<br>www.kraeuterwinkl-menschundtier.de</div>
    <div class="lot">
      <div class="lot__label">Los-Nr. &amp; mind. haltbar bis:</div>
      <div class="lot__box">04/2025<br>731245869</div>
    </div>
  </footer>
</article>

<div class="size-caption size-caption--1000">168X80MM</div>
<article class="label label--1000">
  <header class="label__header">
    <div class="brand-name">KRAEUTERWINKL</div>
    <div class="brand-tagline">FÜR MENSCH &amp; TIER</div>
    <div class="brand-owners">Lena Brandt &amp; Tobias Merz</div>
  </header>
  <div class="label__rule"></div>
  <div class="label__emblem">
    <div class="emblem-art" role="img" aria-label="Illustration: Frau und Hund sitzend in einem Kreis mit Blättern"></div>
  </div>
  <section class="label__body">
    <div class="product-title"><span class="product-title__first">Kolloidales</span> <span class="product-title__second">Silber</span></div>
    <h1 class="product-claim">Antimikrobielle Lösung</h1>
    <hr class="divider">
    <p class="facts">Destilliertes Wasser entmineralisiert<br>Feinsilber Reinheit &gt; 99,99%<br>Kein Lebensmittel</p>
    <hr class="divider">
    <p class="facts facts--storage">Lagerung:<br>Bei Zimmertemperatur dunkel und außerhalb der Reichweite von Kindern lagern. Jegliche Nähe zu elektromagnetischen Feldern vermeiden und nicht mit Metall in Verbindung bringen.</p>
    <p class="facts">Nach dem Öffnen innerhalb von 12 Wochen aufbrauchen</p>
    <hr class="divider">
    <div class="dosage">
      <div class="dosage__options">Konzentration:
        <div class="dosage__choices">
          <span class="choice"><span class="choice__box"></span>25PPM</span>
          <span class="choice"><span class="choice__box"></span>50PPM</span>
          <span class="choice"><span class="choice__box"></span>75PPM</span>
          <span class="choice"><span class="choice__box"></span>100PPM</span>
        </div>
      </div>
      <div class="dosage__volume">1000ML</div>
    </div>
  </section>
  <footer class="label__footer">
    <div class="maker">Hergestellt in Deutschland von:<br>Tobias Merz, Lena Brandt GbR<br>info.kraeuterwinkl@postfach.de<br>www.kraeuterwinkl-menschundtier.de</div>
    <div class="lot">
      <div class="lot__label">Los-Nr. &amp; mind. haltbar bis:</div>
      <div class="lot__box">04/2025<br>731245869</div>
    </div>
  </footer>
</article>

<div class="palette" aria-label="Farbpalette">
  <div class="palette__swatch palette__swatch--teal"></div>
  <div class="palette__swatch palette__swatch--sage"></div>
  <div class="palette__swatch palette__swatch--sand"></div>
  <div class="palette__swatch palette__swatch--stone"></div>
  <div class="palette__swatch palette__swatch--ink"></div>
</div>

</body>
</html>
```